Classic Minimalistic Business Card

Design a classic, minimalistic Business Card. Please find inspiration in the attached Classic Minimalistic examples. My information:
Name: Glen Ovamir
Company: Ovamir Capital
Logo: OC
Address: 1470 N Thornwick Rd, Suite 210 | Geneva, IL 60134
Phone: 630-555-0192
Email: glenovamir@pvt.insure
Slogan: Building Strength Through Capital

Feel free to leave out any of the information above except my name.

I have selected Double-sided, but I am also open to Single-sided

Target Market(s)

22-70. income greater than 150k/year

Industry/Entity Type

Finance

Contact Information for Business Card

See Project Description

Requirements
Must have
• Ivory or "antiqued" background similar to the reference pictures

```html
<!DOCTYPE html>
<html lang="en">
<head>
<meta charset="utf-8">
<title>Ovamir Capital — Business Card</title>
<link rel="stylesheet" href="https://fonts.googleapis.com/css2?family=Monsieur+La+Doulaise&family=Questrial&family=Libre+Baskerville:ital,wght@0,700;1,400&display=swap">
<style>
  :root {
    --backdrop: #989c98;
    --card-ivory: #e5d9c7;
    --ink: #111111;
    --brand-red: #9e3a26;
  }
  html, body {
    margin: 0;
    padding: 0;
    width: 1200px;
    height: 1000px;
    overflow: hidden;
    background: var(--backdrop);
  }
  .business-card {
    position: absolute;
    left: 294px;
    top: 324px;
    width: 613px;
    height: 352px;
    background: var(--card-ivory);
    color: var(--ink);
  }
  .company-name {
    position: absolute;
    left: 0;
    width: 100%;
    top: 64px;
    text-align: center;
    font-family: "Libre Baskerville", serif;
    font-weight: 700;
    font-size: 22px;
    color: var(--brand-red);
    margin: 0;
  }
  .person-name {
    position: absolute;
    left: 0;
    width: 100%;
    top: 118px;
    text-align: center;
    font-family: "Monsieur La Doulaise", cursive;
    font-size: 84px;
    line-height: 1;
    margin: 0;
  }
  .contact-block {
    position: absolute;
    left: 28px;
    width: 300px;
    top: 272px;
    text-align: center;
  }
  .phone {
    display: block;
    font-family: "Questrial", sans-serif;
    font-size: 21px;
    letter-spacing: 2px;
    line-height: 26px;
  }
  .email {
    display: block;
    font-family: "Libre Baskerville", serif;
    font-style: italic;
    font-size: 17px;
    letter-spacing: 1px;
    line-height: 24px;
  }
  .address {
    position: absolute;
    left: 342px;
    width: 240px;
    top: 277px;
    text-align: center;
    font-family: "Questrial", sans-serif;
    font-variant: small-caps;
    font-size: 14px;
    letter-spacing: 1.6px;
    line-height: 15.5px;
    font-style: normal;
    margin: 0;
  }
</style>
</head>
<body>
  <section class="business-card">
    <p class="company-name">Ovamir Capital</p>
    <h1 class="person-name">Glen Ovamir</h1>
    <div class="contact-block">
      <span class="phone">630-555-0192</span>
      <span class="email">glenovamir@pvt.insure</span>
    </div>
    <address class="address">
      1470 N Thornwick Rd,<br>
      Suite 210 Geneva,<br>
      IL 60134
    </address>
  </section>
</body>
</html>
```